Label Design for American Pet Health Startup

We need your help in creating a line-up of labels for our upcoming products. The products will come in two different sizes/shapes. We have a logo (sourced form ArtSquadron!) to start from and a pretty extensive brief (see attached.) The winning design will be bold, simple, and create a strongly branded look to the whole line while allowing consumers to easily sort through the different SKUs.

The logo and other existing design elements are in the attached powerpoint. I will also post some of the source files.

If you choose to compete for this project, please read the creative brief and the powerpoint very carefully before starting.

Thank you for your time and consideration.

Target Market(s)

Pet owners (dog owners, initially) who care deeply about their pets. Their pets are older and may not be thriving the way they once were. The owners want their pets to have the highest quality of life possible, for as long as is practical. They take their pets frequently to the vet and have great faith in veterinary medicine, but they also believe that dietary supplements may have a beneficial effect. They believe this to be possible because they take supplements themselves.

They are probably older--empty nesters or soon to be. They’ve owned their dog for five years or more, or have rescued an older dog from a shelter. Their dog is, in many ways, a full member of their family.

Industry/Entity Type

Pet Care

Font styles to use
Sans Serif

Requirements
Must have
• Please see the attached brief for this detail. I have cut and paste it into this form but it doesn't translate well. Reading the Word document will be easier and the links will work.
• Packaging Creative Considerations: The product packaging needs to . . .
• • Have a strong, branded line look.
• - The logo has already been developed, and I would like you to be guided in your design choices by its structure and color, but I am open to deviations from the existing work if it leads to a strong design
• • Use color or some other design elements to distinguish each SKU from the other
• • Be bold and simple. This product will typically be merchandised online, with very small images of the packaging. Simple and bold design elements will ensure that the products are both noticed and understood.
• - The product will likely be contained within white plastic or aluminum (silver) bottles with white caps/pumps. However, if you believe your design concepts would benefit from a particular color of bottle/container, please illustrate that, as that would be possible to execute.
• • Communicate that these products are for pets without using any clichés. This category is full of packaging with stock photos of dogs and cats. Please avoid this at all costs. Instead, please unleash your creativity to illustrate the products’ nature/purposes.
• A couple of packaging designs I would like you to draw inspiration from:
• o Vemo. This line is for human supplements/vitamins. Notice the strong line look, the simple and bold graphics, and the smart use of color and other design elements to differentiate the SKUs (while still holding it together as a single brand.)
• o Tupka. This line is for pets. Again, notice the strong line look, the smart use of color to differentiate the SKUs, and the simple and bold presentation that translates so well on the screen.
• o Crumblefin. This design is not as good as the first two, but it does accomplish several of the brief’s objectives and the packaging is likely to be very similar to what your design will eventually be affixed to.
• Design Deliverables: A great submission will illustrate its strength by showing how the design translates across all the expected SKUs. To accomplish, this, I would recommend using the “functional maps” I’ve included in the attached Powerpoint document to:
• o First illustrate, in greater size and detail, one SKU each of the two families (one oil SKU and one supplement SKU)
• o Then illustrate how each of those designs extends across the rest of the family. That illustration can be less detailed. We just need to see how the colors and other design elements extend.
Should not have
• No stock images of cats or dogs; please avoid junking up the designs with too many elements

```html
<!DOCTYPE html>
<html lang="en">
<head>
<meta charset="UTF-8">
<title>Tailwell Supplement Labels</title>
<link href="https://fonts.googleapis.com/css2?family=Oswald:wght@300;400;600&family=Lato:wght@300;400&display=swap" rel="stylesheet">
<style>
  :root {
    --page-bg: #d6d6d6;
    --green: #8dc63f;
    --purple: #662d91;
    --black: #050505;
    --white: #ffffff;
    --ink: #1a1a1a;
    --rule: #6e6e6e;
    --dash: #d4d4d4;
    --brand: #1aa6b7;
  }
  html, body {
    margin: 0;
    padding: 0;
    overflow: hidden;
  }
  .canvas {
    position: relative;
    width: 1200px;
    height: 900px;
    background: var(--page-bg);
    overflow: hidden;
  }
  .label {
    position: absolute;
    top: 189px;
    width: 397px;
    height: 436px;
    background: var(--black);
    overflow: hidden;
  }
  .label--hip { left: 177px; --sku: var(--green); }
  .label--skin { left: 616px; --sku: var(--purple); }

  .label__band {
    position: absolute;
    left: 0; top: 0;
    width: 100%;
    height: 154px;
    background: var(--sku);
  }
  .label__stripe {
    position: absolute;
    left: 0; top: 154px;
    width: 100%;
    height: 10px;
    background: var(--white);
  }
  .seal {
    position: absolute;
    left: 68px; top: 20px;
    width: 260px; height: 260px;
    border-radius: 50%;
    background: var(--white);
  }
  .seal__ring {
    position: absolute;
    inset: 9px;
    border-radius: 50%;
    border: 2px dashed var(--dash);
  }
  .brand {
    position: absolute;
    top: 50px; left: 0;
    width: 100%;
    text-align: center;
    font-family: "Lato", sans-serif;
    font-weight: 300;
    font-size: 19px;
    color: var(--brand);
    letter-spacing: 0.5px;
  }
  .brand__dot {
    display: inline-block;
    width: 9px; height: 9px;
    border-radius: 50%;
    background: var(--brand);
    margin-right: 6px;
    vertical-align: middle;
  }
  .seal__rule {
    position: absolute;
    left: 32px;
    width: 196px;
    height: 1px;
    background: var(--rule);
  }
  .seal__rule--top { top: 81px; }
  .seal__rule--bottom { top: 135px; }
  .product-name {
    position: absolute;
    top: 80px; left: 0;
    width: 100%;
    text-align: center;
    font-family: "Oswald", sans-serif;
    font-weight: 600;
    font-size: 45px;
    line-height: 56px;
    color: var(--sku);
    letter-spacing: -0.5px;
  }
  .benefit {
    position: absolute;
    top: 146px; left: 0;
    width: 100%;
    text-align: center;
    font-family: "Lato", sans-serif;
    font-size: 8.6px;
    line-height: 11.5px;
    color: var(--ink);
  }
  .format {
    position: absolute;
    top: 184px; left: 0;
    width: 100%;
    text-align: center;
    font-family: "Oswald", sans-serif;
    font-weight: 400;
    font-size: 9.6px;
    color: var(--sku);
    letter-spacing: -0.2px;
  }
  .pet-icon {
    position: absolute;
    top: 203px; left: 112px;
    width: 36px; height: 32px;
  }
  .claim-badge {
    position: absolute;
    left: 156px; top: 292px;
    width: 84px; height: 84px;
  }
  .net-weight {
    position: absolute;
    top: 384px; left: 0;
    width: 100%;
    text-align: center;
    font-family: "Oswald", sans-serif;
    font-weight: 300;
    font-size: 23px;
    color: var(--sku);
    letter-spacing: -0.5px;
  }
  .origin {
    position: absolute;
    top: 414px; left: 0;
    width: 100%;
    text-align: center;
    font-family: "Lato", sans-serif;
    font-size: 11.5px;
    color: var(--white);
    letter-spacing: 2.6px;
  }
  .count {
    position: absolute;
    left: 340px; top: 358px;
    width: 40px;
    text-align: center;
    font-family: "Oswald", sans-serif;
    color: var(--white);
  }
  .count__number {
    display: block;
    font-weight: 600;
    font-size: 28px;
    line-height: 30px;
  }
  .count__unit {
    display: block;
    font-weight: 300;
    font-size: 9.5px;
    line-height: 11px;
  }
  .count__swatch {
    position: absolute;
    left: 346px; top: 406px;
    width: 28px; height: 30px;
    background: var(--sku);
  }
</style>
</head>
<body>
<main class="canvas">

  <section class="label label--hip">
    <div class="label__band"></div>
    <div class="label__stripe"></div>
    <div class="seal">
      <div class="seal__ring"></div>
      <div class="brand"><span class="brand__dot"></span>Tailwell</div>
      <div class="seal__rule seal__rule--top"></div>
      <h2 class="product-name" style="margin:0">HIP &amp; JOINT</h2>
      <div class="seal__rule seal__rule--bottom"></div>
      <p class="benefit" style="margin:0">SUPPORTS HEALTHY JOINTS WITH<br>GLUCOSAMINE CHONDROITIN, &amp; WILLOW BARK</p>
      <p class="format" style="margin:0">SOFT &amp; CHEWABLE SUPPLEMENTS FOR</p>
      <svg class="pet-icon" viewBox="0 0 36 32" role="img" aria-label="Dog head icon">
        <ellipse cx="18" cy="16" rx="16" ry="15" fill="#050505"/>
      </svg>
    </div>
    <svg class="claim-badge" viewBox="0 0 84 84" role="img" aria-label="Free-from claims badge">
      <circle cx="42" cy="42" r="40" fill="none" stroke="var(--sku)" stroke-width="2"/>
      <circle cx="42" cy="42" r="37" fill="#ffffff"/>
      <circle cx="42" cy="42" r="24" fill="#bdbdbd"/>
    </svg>
    <div class="net-weight">Net Wt 16 OZ / 453 g</div>
    <div class="origin">MADE IN USA</div>
    <div class="count"><span class="count__number">90</span><span class="count__unit">CHEWS</span></div>
    <div class="count__swatch"></div>
  </section>

  <section class="label label--skin">
    <div class="label__band"></div>
    <div class="label__stripe"></div>
    <div class="seal">
      <div class="seal__ring"></div>
      <div class="brand"><span class="brand__dot"></span>Tailwell</div>
      <div class="seal__rule seal__rule--top"></div>
      <h2 class="product-name" style="margin:0">SKIN &amp; COAT</h2>
      <div class="seal__rule seal__rule--bottom"></div>
      <p class="benefit" style="margin:0">SUPPORTS A HEALTHY SKIN &amp; COAT WITH<br>B VITAMINS OMEGA-3, &amp; BIOTIN</p>
      <p class="format" style="margin:0">SOFT &amp; CHEWABLE SUPPLEMENTS FOR</p>
      <svg class="pet-icon" viewBox="0 0 36 32" role="img" aria-label="Dog head icon">
        <ellipse cx="18" cy="16" rx="16" ry="15" fill="#050505"/>
      </svg>
    </div>
    <svg class="claim-badge" viewBox="0 0 84 84" role="img" aria-label="Free-from claims badge">
      <circle cx="42" cy="42" r="40" fill="none" stroke="var(--sku)" stroke-width="2"/>
      <circle cx="42" cy="42" r="37" fill="#ffffff"/>
      <circle cx="42" cy="42" r="24" fill="#bdbdbd"/>
    </svg>
    <div class="net-weight">Net Wt 16 OZ / 453 g</div>
    <div class="origin">MADE IN USA</div>
    <div class="count"><span class="count__number">90</span><span class="count__unit">CHEWS</span></div>
    <div class="count__swatch"></div>
  </section>

</main>
</body>
</html>
```